Poster Design Project- New Years Eve

We are a fun and quirky bar in St Kilda (www.coppernook.com.au). We need a poster designed for our New Years Eve Event- details as follows
Project: A1 poster-NYE
Name of Event: Lucky Comets
Date of Event: New Years Eve: 31.12.12
Tagline: ‘What happens at Nook stays at Nook’
Time: 8pm-3am
Cost:
$105 all inclusive
-Includes a cocktail on arrival
-4 hour drink package – Basic Spirits, Premium Beer, Wine and Sparkling til 12AM
-Grazing style canapés and finger food
Early bird and group discounts (10+) available
Purchase your tickets at the bar or through the website
Dress: For Fun and Dancing
Venue information:
• Address: 14 Harwell Lane St Kilda
• Phone: 9413 6057
• Email: info@coppernook.com.au
• Website: www.coppernook.com.au
• Management reserves the right to refuse entry
Images: Images need to be high resolution or vector images so clarity is not lost when the poster is blown up to this size
Poster production:
Poster needs to be created in either Adobe Illustrator or Photoshop so we can easily edit the details if they change after the contest ends
Please provide 3mm internal and external bleed
Theming:
Fun poster with elements of Las Vegas including: dice/casino element, Las Lucky Comets, pretty girls, cocktails
Target Market(s)
25-40 year olds
Industry/Entity Type
Casino

```html
<!DOCTYPE html>
<html lang="en">
<head>
<meta charset="utf-8">
<title>Lucky Comets – New Years Eve at Copper Nook</title>
<link rel="stylesheet" href="https://fonts.googleapis.com/css2?family=Anton&family=Great+Vibes&family=Roboto+Condensed:wght@700&family=Arimo:wght@400;700&display=swap">
<style>
  :root {
    --night: #050505;
    --glow-green: #5fe01a;
    --glow-lime: #c6e51c;
    --glow-blue: #1b3f8f;
    --glow-violet: #4a2a7a;
    --gold: #ffe21a;
    --gold-deep: #e0a800;
    --lavender: #f3e8ff;
    --violet-edge: #8a2bd6;
    --white: #ffffff;
  }
  html, body {
    margin: 0;
    padding: 0;
    overflow: hidden;
    background: var(--night);
  }
  .poster {
    position: relative;
    width: 1200px;
    height: 880px;
    overflow: hidden;
    background: var(--night);
    font-family: "Arimo", Arial, sans-serif;
    color: var(--white);
  }
  .party-scene {
    position: absolute;
    inset: 0;
    background:
      radial-gradient(ellipse 420px 260px at 560px 300px, rgba(230,200,40,0.55), transparent 70%),
      radial-gradient(ellipse 700px 380px at 650px 120px, var(--glow-green), transparent 70%),
      radial-gradient(ellipse 380px 300px at 80px 120px, var(--glow-blue), transparent 70%),
      radial-gradient(ellipse 420px 300px at 1150px 120px, var(--glow-violet), transparent 70%),
      linear-gradient(180deg, #2a5a20 0%, #1b2a14 38%, #0a0a0a 58%, var(--night) 100%);
  }
  .title {
    position: absolute;
    left: 0;
    top: 92px;
    width: 1200px;
    text-align: center;
  }
  .title-main {
    display: block;
    font-family: "Anton", Impact, sans-serif;
    font-size: 150px;
    line-height: 1;
    letter-spacing: 14px;
    padding-left: 14px;
    background: linear-gradient(180deg, #fff36a 0%, var(--gold) 45%, var(--gold-deep) 100%);
    -webkit-background-clip: text;
    background-clip: text;
    color: transparent;
  }
  .title-script {
    position: absolute;
    left: 590px;
    top: 95px;
    font-family: "Great Vibes", cursive;
    font-size: 92px;
    line-height: 1;
    color: var(--white);
    text-shadow: 0 0 3px rgba(80,40,0,0.8);
  }
  .headline {
    position: absolute;
    left: 0;
    width: 1200px;
    text-align: center;
    font-family: "Roboto Condensed", "Arial Narrow", sans-serif;
    font-weight: 700;
    color: var(--lavender);
    text-shadow:
      -1px -1px 0 var(--violet-edge), 1px -1px 0 var(--violet-edge),
      -1px 1px 0 var(--violet-edge), 1px 1px 0 var(--violet-edge),
      0 0 6px rgba(138,43,214,0.7);
    margin: 0;
  }
  .headline-date { top: 328px; font-size: 40px; }
  .headline-tagline { top: 388px; font-size: 46px; }
  .headline-time { top: 446px; font-size: 36px; }
  .offer {
    position: absolute;
    left: 40px;
    top: 512px;
  }
  .offer-price {
    margin: 0 0 10px;
    font-size: 25px;
    color: var(--gold);
    letter-spacing: 0.5px;
  }
  .offer-list {
    list-style: none;
    margin: 0;
    padding: 0;
  }
  .offer-list li {
    position: relative;
    padding-left: 24px;
    font-size: 16px;
    letter-spacing: 0.8px;
    line-height: 24px;
  }
  .offer-list svg {
    position: absolute;
    left: 0;
    top: 6px;
    width: 11px;
    height: 11px;
  }
  .booking {
    position: absolute;
    left: 40px;
    top: 664px;
    margin: 0;
    font-size: 17px;
    line-height: 23px;
    color: var(--gold);
  }
  .dress-code {
    position: absolute;
    left: 40px;
    top: 734px;
    margin: 0;
    font-size: 17px;
    color: var(--gold);
  }
  .venue {
    position: absolute;
    left: 40px;
    top: 796px;
    font-size: 13.5px;
    letter-spacing: 0.3px;
  }
  .venue p { margin: 0 0 6px; }
  .venue .sep {
    display: inline-block;
    width: 3px;
    height: 12px;
    background: var(--white);
    margin: 0 9px;
    vertical-align: -1px;
  }
  .venue .notice { margin-top: 12px; }
  .venue-name {
    position: absolute;
    left: 680px;
    top: 680px;
    font-family: "Arimo", Arial, sans-serif;
    font-weight: 700;
    font-size: 60px;
    line-height: 1;
    color: var(--white);
  }
</style>
</head>
<body>
<main class="poster">
  <div class="party-scene" role="img" aria-label="Glowing green and gold disco ball with a dancing crowd in silhouette"></div>

  <h1 class="title">
    <span class="title-main">LUCKY</span>
    <span class="title-script">Comets</span>
  </h1>

  <p class="headline headline-date">NEW YEARS EVE: 31.12.12</p>
  <p class="headline headline-tagline">WHAT HAPPENS AT NOOK STAYS AT NOOK</p>
  <p class="headline headline-time">8PM-3AM</p>

  <section class="offer">
    <h2 class="offer-price">$105 ALL INCLUSIVE</h2>
    <ul class="offer-list">
      <li><svg viewBox="0 0 10 10"><polygon points="5,0 6.2,3.6 10,3.6 6.9,5.8 8.1,9.5 5,7.2 1.9,9.5 3.1,5.8 0,3.6 3.8,3.6" fill="#fff"/></svg>INCLUDES A COCKTAIL ON ARRIVAL</li>
      <li><svg viewBox="0 0 10 10"><polygon points="5,0 6.2,3.6 10,3.6 6.9,5.8 8.1,9.5 5,7.2 1.9,9.5 3.1,5.8 0,3.6 3.8,3.6" fill="#fff"/></svg>4 HOUR DRINK PACKAGE - BASIC SPIRITS, PREMIUM BEER,WINE AND SPARKLING TIL 12AM</li>
      <li><svg viewBox="0 0 10 10"><polygon points="5,0 6.2,3.6 10,3.6 6.9,5.8 8.1,9.5 5,7.2 1.9,9.5 3.1,5.8 0,3.6 3.8,3.6" fill="#fff"/></svg>GRAZING STYLE CANAPES AND FINGER FOOD</li>
    </ul>
  </section>

  <p class="booking">EARLY BIRD AND GROUP DISCOUNTS (10+) AVAILABLE<br>PURCHASE YOUR TICKETS AT THE BAR OR THROUGH THE WEBSITE</p>
  <p class="dress-code">DRESS: FOR FUN AND DANCING</p>

  <div class="venue-name">Copper Nook</div>

  <footer class="venue">
    <p>VENUE INFORMATION:</p>
    <p>14 HARWELL LANE ST KILDA<span class="sep"></span>9413 6057<span class="sep"></span>INFO@COPPERNOOK.COM.AU<span class="sep"></span>WWW.COPPERNOOK.COM.AU</p>
    <p class="notice">MANAGEMENT RESERVES THE RIGHT TO REFUSE ENTRY</p>
  </footer>
</main>
</body>
</html>
```